HK-Steuerberatung WordPress Site fully implemented (tax advisor)

Hello!
I need a little Wordpress Site for my newly founded Tax-Advisor Company.
I am a one-man Office advising in the area of Crypto-Currency.
PLEASE only provide a Design, if you can also Implement a WP-Site afterwards on an existing Webspace.

Please find the Content and Website-Description in the attached Document

Language for the Website is German (for now)

Target Market(s)

Tax-Advisory (specialized in Crypto Currency)

Coding

Coded - Design and coding required

Number of Pages Required

5+ page

Font styles to use
Sans Serif

Requirements
Must have
• Wordpress Implementation afterwards - Details according to attached Project Information Document

```html
<!DOCTYPE html>
<html lang="de">
<head>
<meta charset="utf-8">
<title>HK-Steuerberatung</title>
<link href="https://fonts.googleapis.com/css2?family=Montserrat:wght@400;500;600;700;800&display=swap" rel="stylesheet">
<style>
:root{
  --navy:#1b2a44;
  --navy-deep:#0b1628;
  --teal:#14a6ac;
  --text:#3c4350;
  --muted:#8a909a;
  --light:#eff0f2;
  --icon-bg:#eeeff1;
  --line:#e6e7ea;
  --white:#ffffff;
}
*{box-sizing:border-box;margin:0;padding:0}
html,body{width:1200px;height:2931px;overflow:hidden}
body{font-family:"Montserrat",sans-serif;color:var(--text);background:var(--white);position:relative}
.abs{position:absolute}
a{color:inherit;text-decoration:none}

/* header */
.site-header{position:absolute;left:0;top:0;width:1200px;height:80px}
.brand{left:128px;top:26px;display:flex;align-items:center;gap:10px;font-weight:700;font-size:15px;color:var(--navy);letter-spacing:.3px}
.brand-mark{width:26px;height:26px;background:var(--navy);border-radius:4px}
.main-nav{left:494px;top:33px;display:flex;gap:18px;font-size:9px;font-weight:500;letter-spacing:.4px;color:var(--navy)}
.main-nav .active{color:var(--teal);border-bottom:1px solid var(--teal);padding-bottom:5px}
.nav-sep{left:849px;top:32px;width:1px;height:10px;background:#c9ccd2}
.nav-phone{left:871px;top:33px;font-size:9px;color:var(--navy);display:flex;gap:6px;align-items:center}
.btn-start{left:970px;top:26px;width:101px;height:25px;background:var(--teal);color:var(--white);font-size:9px;font-weight:600;display:flex;align-items:center;justify-content:center;gap:6px;border-radius:2px;letter-spacing:.4px}

/* hero */
.hero{position:absolute;left:0;top:0;width:1200px;height:592px;background:linear-gradient(180deg,#f7f7f8 0%,#ebecee 25%,#ebecee 100%)}
.hero-title{left:209px;top:194px;font-size:46px;line-height:51px;font-weight:800;color:var(--navy);letter-spacing:.5px}
.hero-sub{left:209px;top:306px;font-size:15px;font-weight:700;color:var(--navy)}
.hero-sub span{color:var(--teal);margin-right:6px}
.hero-desc{left:209px;top:340px;font-size:11px;color:var(--text)}
.link-ring{display:flex;align-items:center;font-size:10px;font-weight:600;letter-spacing:.8px;color:var(--navy)}
.link-ring::before{content:"";width:30px;height:30px;border-radius:50%;background:#dcdde0;margin-right:-11px}
.hero-link{left:209px;top:375px}

/* services */
.eyebrow{font-size:9px;font-weight:600;letter-spacing:3px;color:var(--teal);display:flex;align-items:center;gap:8px}
.eyebrow::after{content:"";width:12px;height:1px;background:#d4d6da}
.eyebrow.center::before{content:"";width:12px;height:1px;background:#d4d6da}
.section-title{font-size:33px;font-weight:800;color:var(--navy);letter-spacing:.3px}
.services-label{left:209px;top:657px}
.services-title{left:209px;top:676px}
.services-intro{left:209px;top:718px;width:740px;font-size:11px;line-height:17px}
.service{position:absolute;width:210px;font-size:11px;line-height:17px}
.service-icon{width:57px;height:57px;border-radius:6px;background:var(--icon-bg);display:flex;align-items:center;justify-content:center;margin-bottom:27px}
.service-icon.is-active{background:var(--teal)}
.service a{color:var(--teal);font-weight:600}
.tags{display:flex;flex-wrap:wrap;gap:4px;margin-top:3px;width:190px}
.tag{background:var(--teal);color:var(--white);font-size:8px;font-weight:700;padding:1px 6px}
.divider{position:absolute;left:0;width:1200px;height:1px;background:var(--line)}

/* cta */
.cta-text{left:0;top:1236px;width:1200px;text-align:center;font-size:20px;line-height:25px;font-weight:700;color:var(--navy)}
.cta-link{left:522px;top:1339px}

/* kollegen */
.colleagues{position:absolute;left:0;top:1445px;width:1200px;height:477px;background:var(--light)}
.art{border-radius:40px;background:radial-gradient(circle at 60% 40%,#14304c 0%,var(--navy-deep) 70%)}
.colleagues-art{left:209px;top:1507px;width:303px;height:353px}
.colleagues-label{left:610px;top:1529px}
.colleagues-title{left:610px;top:1548px;font-size:32px;line-height:38px}
.body-text{font-size:11px;line-height:17px}
.colleagues-text{left:610px;top:1630px;width:380px}
.body-text p+p{margin-top:6px}
.colleagues-link{left:610px;top:1793px}

/* about */
.about-label{left:209px;top:2005px}
.about-title{left:209px;top:2024px}
.about-text{left:209px;top:2070px;width:380px}
.btn-primary{left:209px;top:2300px;width:215px;height:31px;background:var(--teal);color:var(--white);font-size:10px;font-weight:600;letter-spacing:.5px;display:flex;align-items:center;justify-content:center}
.about-art{left:688px;top:1983px;width:304px;height:352px}
.about-photo{left:643px;top:2098px;width:96px;height:98px;border:3px solid var(--white);background:linear-gradient(160deg,#b8c6d6 0%,#6f7d8c 55%,#3a4250 100%)}

/* contact */
.contact-label{left:0;top:2466px;width:1200px;justify-content:center}
.contact-title{left:0;top:2486px;width:1200px;text-align:center}
.contact-text{left:250px;top:2528px;width:700px;text-align:center;font-size:11px;line-height:17px}
.contact-link{left:522px;top:2586px}

/* footer */
.site-footer{position:absolute;left:0;top:2687px;width:1200px;height:244px;background:var(--navy);color:var(--white);text-align:center}
.footer-mark{left:586px;top:38px;width:28px;height:28px;border-radius:4px;background:var(--white)}
.footer-brand{left:0;top:96px;width:1200px;font-size:17px;font-weight:700;letter-spacing:.3px}
.copyright{left:0;top:128px;width:1200px;font-size:8px;letter-spacing:.6px;color:#8f99ab}
.footer-links{left:0;top:149px;width:1200px;font-size:9px;font-weight:600;letter-spacing:.5px;display:flex;justify-content:center;gap:22px}
.socials{left:0;top:178px;width:1200px;display:flex;justify-content:center;align-items:center;gap:10px}
.social{width:10px;height:10px;border-radius:50%;background:var(--white)}
.social.is-active{width:24px;height:24px;background:var(--teal);position:relative}
.social.is-active::after{content:"";position:absolute;left:8px;top:8px;width:8px;height:8px;border-radius:50%;background:var(--white)}
.to-top{left:594px;top:223px}
</style>
</head>
<body>

<section class="hero" aria-label="Einleitung">
  <h1 class="abs hero-title">WILLKOMMEN BEI<br>HK-STEUERBERATUNG!</h1>
  <p class="abs hero-sub"><span>02</span>Dann melde ich einfach meinen Hauptwohnsitz in Österreich ab</p>
  <p class="abs hero-desc">Ihrem Spezialisten bei allen steuerlichen Themen rund um Einkünfte &amp; Vermögen aus Krypto-Assets.</p>
  <a class="abs link-ring hero-link" href="#leistungen">WEITER ZU UNSEREN LEISTUNGEN</a>
</section>

<header class="site-header">
  <div class="abs brand"><span class="brand-mark"></span>HK STEUERBERATUNG</div>
  <nav class="abs main-nav">
    <a class="active" href="#">HOME</a><a href="#">LEISTUNGEN</a><a href="#">KOLLEGENDIENST</a><a href="#">ÜBER MICH</a><a href="#">KONTAKT</a>
  </nav>
  <span class="abs nav-sep"></span>
  <div class="abs nav-phone">
    <svg width="9" height="9" viewBox="0 0 24 24" fill="none" stroke="#1b2a44" stroke-width="2"><path d="M5 3h4l2 5-2.5 1.5a11 11 0 0 0 6 6L16 13l5 2v4a2 2 0 0 1-2 2A17 17 0 0 1 3 5a2 2 0 0 1 2-2z"/></svg>
    +43 512 000 111
  </div>
  <a class="abs btn-start" href="#">
    <svg width="9" height="9" viewBox="0 0 24 24" fill="none" stroke="#fff" stroke-width="2.5"><rect x="3" y="3" width="18" height="18" rx="2"/><path d="M8 16l8-8"/></svg>
    LOSLEGEN
  </a>
</header>

<section id="leistungen" aria-label="Leistungen">
  <div class="abs eyebrow services-label">LEISTUNGEN</div>
  <h2 class="abs section-title services-title">WAS WIR TUN</h2>
  <p class="abs services-intro">Ich biete in meiner Kanzlei ausschließlich Spezialberatung rund um die komplexen und vielseitigen Themen im Krypto-Bereich sowie deren Besteuerung, bzw. der Besteuerung und steuerlichen Optimierung von anderen passiven Einkommensmodellen an:</p>

  <div class="service" style="left:209px;top:796px">
    <div class="service-icon"><svg width="22" height="22" viewBox="0 0 24 24" fill="none" stroke="#1b2a44" stroke-width="1.3"><circle cx="12" cy="12" r="5"/><circle cx="12" cy="12" r="9"/></svg></div>
    Steueroptimales Besitzen von KryptoAssets auf in- und ausländischen Börsen
  </div>
  <div class="service" style="left:476px;top:796px">
    <div class="service-icon is-active"><svg width="22" height="22" viewBox="0 0 24 24" fill="none" stroke="#fff" stroke-width="1.3"><rect x="4" y="5" width="16" height="15"/><path d="M4 10h16M9 5v15M15 5v15"/></svg></div>
    Finanzstrafrechtliche Offenlegung und Aufarbeitung bei Einkünften die nicht ordnungsgemäß erklärt wurden
  </div>
  <div class="service" style="left:743px;top:796px">
    <div class="service-icon"><svg width="22" height="22" viewBox="0 0 24 24" fill="none" stroke="#1b2a44" stroke-width="1.3"><circle cx="12" cy="12" r="9"/><path d="M3 12h18M12 3c3 3 3 15 0 18M12 3c-3 3-3 15 0 18"/></svg></div>
    Hilfe bei der korrekten Erklärung der Crypto-Einkünfte und Erstellung der Steuererklärungen
  </div>
  <div class="service" style="left:209px;top:950px">
    <div class="service-icon"><svg width="22" height="22" viewBox="0 0 24 24" fill="none" stroke="#1b2a44" stroke-width="1.3"><circle cx="12" cy="12" r="4"/><circle cx="12" cy="12" r="8" stroke-dasharray="3 2"/></svg></div>
    Hilfestellung bei der Dokumentation der Einkünfte <a href="#">Verwendung von Tax-Tools und Aufbereitung der Daten</a>
  </div>
  <div class="service" style="left:476px;top:950px">
    <div class="service-icon"><svg width="22" height="22" viewBox="0 0 24 24" fill="none" stroke="#1b2a44" stroke-width="1.3"><circle cx="12" cy="12" r="9"/><path d="M5 7c5 2 9 7 11 13M9 3c1 6 6 10 12 10"/></svg></div>
    Beratung rund um das Thema Wegzug, Wohnsitzverlegung und in-/ausländische Gesellschaften
  </div>
  <div class="service" style="left:743px;top:950px">
    <div class="service-icon"><svg width="22" height="22" viewBox="0 0 24 24" fill="none" stroke="#1b2a44" stroke-width="1.3"><circle cx="12" cy="11" r="5"/><path d="M10 17h4M10 20h4M12 2v2M4 11H2M22 11h-2"/></svg></div>
    Beratung bei der Unterscheidung und Besteuerung der diversen Einkunftsmöglichkeiten.
    <div class="tags"><span class="tag">TRADING</span><span class="tag">STAKING</span><span class="tag">LENDING</span><span class="tag">MININGVNODES</span><span class="tag">NFTS</span></div>
  </div>
</section>

<div class="divider" style="top:1174px"></div>

<section aria-label="Klassische Services">
  <p class="abs cta-text">Werden neben der Spezialberatung auch noch klassische Services<br>wie Buchhaltung, Lohnverrechnung etc. benötigt, kann dies gerne<br>über Partner-Kanzleien von mir organisiert werden.</p>
  <a class="abs link-ring cta-link" href="#kontakt">KONTAKTIERE MICH!</a>
</section>

<section class="colleagues" aria-label="Kollegendienst"></section>
<div class="abs art colleagues-art" role="img" aria-label="Abstrakte dunkelblaue Grafik mit Netzwerkpunkten"></div>
<div class="abs eyebrow colleagues-label">KOLLEGENDIENST</div>
<h2 class="abs section-title colleagues-title">TRADITIONELLEN<br>STEUERBERATUNG</h2>
<div class="abs body-text colleagues-text">
  <p>Ihr Fokus liegt in der traditionellen Steuerberatung und Sie haben keine Zeit sich das hochkomplexe Spezialthema Kryptowährungen etc. einzuarbeiten?</p>
  <p>Um Ihre Klienten dennoch weiterhin vollumfänglich beraten zu können, biete ich Ihnen gerne mein Know-How und die gesamte Leistungspalette an um Ihre Kunden ganz nach Ihrem Wunsch entweder direkt oder diskret im Hintergrund bei sämtlichen Themen rund um Krypto mit steuerlicher Expertise dazu zu unterstützen.</p>
</div>
<a class="abs link-ring colleagues-link" href="#kontakt">KONTAKTIERE MICH!</a>

<section aria-label="Über mich">
  <div class="abs eyebrow about-label">ÜBER MICH</div>
  <h2 class="abs section-title about-title">MARKUS LEHNER</h2>
  <div class="abs body-text about-text">
    <p>Mag. Markus Lehner Ich blicke auf eine sehr umfassende Ausbildung und langjährige Berufserfahrung in der IT Branche zurück. Nach Abschluss des Wirtschaftsstudiums habe ich den klassischen Weg der Steuerberaterausbildung absolviert und bin in diesem Bereich seit über 13 Jahren beratend tätig.</p>
    <p>Durch die Kombination meines umfassenden Wissens in der IT und der Wirtschaft habe ich schon immer gerne Unternehmen mit besonderes technischen oder digitalen Geschäftsmodellen beraten. Seit mehreren Jahren bin ich privat an der Blockchaintechnologie und dem Krypto-Universum interessiert und bereits seit dem Jahre 2017 ist dieses Thema auch Teil meiner fixen Beratungsfelder in der Steuerberatung.</p>
  </div>
  <a class="abs btn-primary" href="#">AUSBILDUNG UND WERDEGANG</a>
  <div class="abs art about-art" role="img" aria-label="Abstrakte dunkelblaue Grafik mit Netzwerkpunkten"></div>
  <div class="abs about-photo" role="img" aria-label="Porträtfoto des Steuerberaters"></div>
</section>

<div class="divider" style="top:2400px"></div>

<section id="kontakt" aria-label="Kontakt">
  <div class="abs eyebrow center contact-label">KONTAKT</div>
  <h2 class="abs section-title contact-title">WIR SIND HIER UM ZU HELFEN</h2>
  <p class="abs contact-text">Wenn Sie Fragen oder Wünsche zu unserem Unternehmen oder den von uns angebotenen Dienstleistungen haben, rufen Sie uns bitte an, senden Sie uns eine E-Mail oder verwenden Sie das untenstehende Formular.</p>
  <a class="abs link-ring contact-link" href="#">KONTAKT FORMULAR</a>
</section>

<footer class="site-footer">
  <span class="abs footer-mark"></span>
  <div class="abs footer-brand">HK STEUERBERATUNG</div>
  <p class="abs copyright">© COPYRIGHT 2022 HK-STEUERBERATUNG. ALL RIGHTS RESERVED</p>
  <nav class="abs footer-links"><a href="#">IMPRESSUM</a><a href="#">PRIVACY POLICY</a></nav>
  <div class="abs socials"><span class="social"></span><span class="social is-active"></span><span class="social"></span></div>
  <svg class="abs to-top" width="12" height="7" viewBox="0 0 12 7" fill="none" stroke="#6c7890" stroke-width="1.3"><path d="M1 6l5-5 5 5"/></svg>
</footer>

</body>
</html>
```